Family Values Poster

Need a poster for my kids (ages 5-8) that says:
Be Smart
Be Kind
Be Curious
Be Grateful
We Love You

fun, but hopefully something that they will keep for a long time

Target Market(s)

my kids

Requirements
Must have
• vertical
Nice to have
• fun and attention grabbing
Should not have
• look cheesy - not a generic inspirational poster

```html
<!DOCTYPE html>
<html lang="en">
<head>
<meta charset="UTF-8">
<title>Be Smart, Be Kind – Family Values Poster</title>
<link rel="stylesheet" href="https://fonts.googleapis.com/css2?family=Montserrat:wght@900&display=swap">
<style>
  :root {
    --navy: #1f3358;
    --blue: #1f5a7a;
    --teal: #1f8f8a;
    --teal-light: #3bb0a0;
    --slate: #6b7a80;
    --peach: #e3a878;
    --orange: #ec8a33;
    --amber: #f4a83c;
    --rust: #b5431f;
    --brown: #6e2414;
    --ink: #ffffff;
  }
  html, body {
    margin: 0;
    padding: 0;
    overflow: hidden;
    background: #ffffff;
  }
  .poster {
    position: relative;
    width: 848px;
    height: 1200px;
    overflow: hidden;
  }
  .poster__art {
    position: absolute;
    inset: 0;
    display: block;
  }
  .poster__words {
    position: absolute;
    inset: 0;
    display: block;
  }
  .poster__line {
    font-family: "Montserrat", sans-serif;
    font-weight: 900;
    fill: var(--ink);
  }
</style>
</head>
<body>
<main class="poster">
  <svg class="poster__art" width="848" height="1200" viewBox="0 0 848 1200" role="img" aria-label="Low-poly geometric background fading from deep blue and teal at the top to orange and rust at the bottom">
    <defs>
      <linearGradient id="bg-main" x1="0" y1="0" x2="0.35" y2="1">
        <stop offset="0" stop-color="var(--navy)"/>
        <stop offset="0.18" stop-color="var(--teal)"/>
        <stop offset="0.34" stop-color="var(--teal-light)"/>
        <stop offset="0.48" stop-color="var(--slate)"/>
        <stop offset="0.6" stop-color="var(--peach)"/>
        <stop offset="0.75" stop-color="var(--orange)"/>
        <stop offset="0.9" stop-color="var(--rust)"/>
        <stop offset="1" stop-color="var(--brown)"/>
      </linearGradient>
      <radialGradient id="bg-glow-amber" cx="0.5" cy="0.78" r="0.35">
        <stop offset="0" stop-color="var(--amber)" stop-opacity="0.8"/>
        <stop offset="1" stop-color="var(--amber)" stop-opacity="0"/>
      </radialGradient>
      <radialGradient id="bg-shade-right" cx="1" cy="0.45" r="0.35">
        <stop offset="0" stop-color="var(--brown)" stop-opacity="0.75"/>
        <stop offset="1" stop-color="var(--brown)" stop-opacity="0"/>
      </radialGradient>
      <radialGradient id="bg-shade-left" cx="0" cy="0.15" r="0.4">
        <stop offset="0" stop-color="var(--navy)" stop-opacity="0.8"/>
        <stop offset="1" stop-color="var(--navy)" stop-opacity="0"/>
      </radialGradient>
    </defs>
    <rect width="848" height="1200" fill="url(#bg-main)"/>
    <rect width="848" height="1200" fill="url(#bg-glow-amber)"/>
    <rect width="848" height="1200" fill="url(#bg-shade-right)"/>
    <rect width="848" height="1200" fill="url(#bg-shade-left)"/>
  </svg>

  <svg class="poster__words" width="848" height="1200" viewBox="0 0 848 1200">
    <text class="poster__line poster__line--smart" x="96" y="328" font-size="133" textLength="656" lengthAdjust="spacingAndGlyphs">BE SMART</text>
    <text class="poster__line poster__line--kind" x="96" y="456" font-size="167" textLength="656" lengthAdjust="spacingAndGlyphs">BE KIND</text>
    <text class="poster__line poster__line--curious" x="96" y="543" font-size="111" textLength="656" lengthAdjust="spacingAndGlyphs">BE CURIOUS</text>
    <text class="poster__line poster__line--grateful" x="96" y="622" font-size="101" textLength="656" lengthAdjust="spacingAndGlyphs">BE GRATEFUL</text>
    <text class="poster__line poster__line--love" x="96" y="736" font-size="147" textLength="656" lengthAdjust="spacingAndGlyphs">WE LOVE</text>
    <text class="poster__line poster__line--you" x="96" y="966" font-size="313" textLength="656" lengthAdjust="spacingAndGlyphs">YOU</text>
  </svg>
</main>
</body>
</html>
```